Need a business card for auto body business

Needs to be on card:
Ridge Crest Collision Marco Bellanti / Licensed Appraiser PGRC Corp LinkCircle Logo
418 Orchard Avenue
Maplebrook MA 02597
T 617-555-0193
F 781-555-0147
pinegroveridgecrest.com
info@pinegroveridgecrest.com
https://www.linkcircle.net/Ridge.Crest.Collision

I will attach a sample of the old Business card

Target Market(s)

Professional, business, classy,

Industry/Entity Type

Business

```html
<!DOCTYPE html>
<html lang="en">
<head>
<meta charset="utf-8">
<title>Ridge Crest Collision – Business Card</title>
<link rel="stylesheet" href="https://fonts.googleapis.com/css2?family=Philosopher:wght@400;700&family=Federo&display=swap">
<style>
  :root {
    --card-orange: #f7901e;
    --band-red: #ec2227;
    --band-edge: #ffc72c;
    --cream: #fff4e0;
    --brand-red: #9b2a2c;
    --white: #ffffff;
  }
  * { margin: 0; padding: 0; box-sizing: border-box; }
  html, body { width: 1200px; height: 702px; overflow: hidden; background: var(--card-orange); }
  .card {
    position: relative;
    width: 1200px;
    height: 702px;
    background: var(--card-orange);
    overflow: hidden;
  }
  .brand {
    position: absolute;
    left: 0; right: 0;
    top: 140px;
    display: flex;
    justify-content: center;
    align-items: center;
    gap: 16px;
  }
  .brand-dot {
    width: 26px; height: 26px;
    border-radius: 50%;
    background: var(--brand-red);
  }
  .brand-name {
    font-family: "Philosopher", sans-serif;
    font-weight: 700;
    font-size: 46px;
    color: var(--brand-red);
    letter-spacing: 1px;
  }
  .corp-band {
    position: absolute;
    left: 59px;
    top: 293px;
    width: 1082px;
    height: 149px;
    background: var(--band-red);
    border-top: 4px solid var(--band-edge);
    border-bottom: 4px solid var(--band-edge);
    display: flex;
    align-items: center;
    justify-content: center;
  }
  .corp-name {
    font-family: "Philosopher", sans-serif;
    font-weight: 400;
    font-size: 113px;
    color: var(--cream);
    line-height: 1;
    margin-top: -6px;
  }
  .person {
    position: absolute;
    left: 71px;
    top: 518px;
    color: var(--cream);
    font-family: "Federo", sans-serif;
  }
  .person-name {
    font-size: 54px;
    letter-spacing: 1.5px;
    line-height: 1;
    text-transform: uppercase;
  }
  .person-title {
    margin-top: 10px;
    font-size: 29px;
    line-height: 1;
    text-transform: uppercase;
  }
  .contact-list {
    position: absolute;
    left: 628px;
    top: 470px;
    list-style: none;
    font-family: "Federo", sans-serif;
    font-size: 21.5px;
    color: var(--cream);
  }
  .contact-item {
    display: flex;
    align-items: center;
    height: 28.4px;
    white-space: nowrap;
  }
  .contact-icon {
    width: 24px; height: 20px;
    margin-right: 13px;
    flex: none;
  }
  .contact-icon svg { width: 100%; height: 100%; display: block; fill: var(--white); }
</style>
</head>
<body>
<main class="card">
  <div class="brand">
    <span class="brand-dot"></span>
    <span class="brand-name">Ridge Crest Collision</span>
  </div>

  <div class="corp-band">
    <h1 class="corp-name">PGRC Corp</h1>
  </div>

  <div class="person">
    <p class="person-name">Marco Bellanti</p>
    <p class="person-title">Owner . Licensed Appraiser</p>
  </div>

  <ul class="contact-list">
    <li class="contact-item">
      <span class="contact-icon"><svg viewBox="0 0 24 20"><path d="M12 1 L23 10 H20 V19 H14.5 V13 H9.5 V19 H4 V10 H1 Z"/></svg></span>
      418 Orchard Avenue, Maplebrook Ma 02597
    </li>
    <li class="contact-item">
      <span class="contact-icon"><svg viewBox="0 0 24 20"><rect x="7" y="1" width="10" height="18" rx="2"/><rect x="9" y="3.5" width="6" height="10" fill="#f7901e"/></svg></span>
      617-555-0193
    </li>
    <li class="contact-item">
      <span class="contact-icon"><svg viewBox="0 0 24 20"><rect x="7" y="2" width="10" height="5"/><rect x="3" y="7" width="18" height="8" rx="2"/><rect x="7" y="13" width="10" height="5"/></svg></span>
      781-555-0147
    </li>
    <li class="contact-item">
      <span class="contact-icon"><svg viewBox="0 0 24 20"><circle cx="12" cy="10" r="8"/><path d="M4 10 H20 M12 2 C8 6 8 14 12 18 M12 2 C16 6 16 14 12 18 M5.5 6 H18.5 M5.5 14 H18.5" stroke="#f7901e" stroke-width="1.3" fill="none"/></svg></span>
      www.pinegroveridgecrest.com
    </li>
    <li class="contact-item">
      <span class="contact-icon"><svg viewBox="0 0 24 20"><rect x="7" y="5" width="16" height="12" rx="1"/><path d="M7.5 5.5 L15 12 L22.5 5.5" stroke="#f7901e" stroke-width="1.5" fill="none"/><path d="M0 8 H5 M1.5 11 H5 M3 14 H5" stroke="#ffffff" stroke-width="1.2"/></svg></span>
      info@pinegroveridgecrest.com
    </li>
    <li class="contact-item">
      <span class="contact-icon"><svg viewBox="0 0 24 20"><circle cx="12" cy="10" r="6"/></svg></span>
      https://www.linkcircle.net/Ridge.Crest.Collision
    </li>
  </ul>
</main>
</body>
</html>
```